Crestline Gas and Plumbing Business Card Design

I am after a business card design for my plumbing business called 'Crestline Gas & Plumbing'. I do all types of plumbing and gas work and specialise in general maintenance plumbing. Would like to see designs using current logo

Industry/Entity Type

Plumbing

Contact Information for Business Card

Name - Dale Whitcombe
Phone number - 0455163027
Email - admin@crestlinegasandplumbing.example.com.au
ABN - 68204915336

```html
<!DOCTYPE html>
<html lang="en">
<head>
<meta charset="utf-8">
<title>Crestline Gas &amp; Plumbing – Business Card</title>
<link rel="stylesheet" href="https://fonts.googleapis.com/css2?family=Exo+2:wght@400;600;800&display=swap">
<style>
  :root {
    --board: #8a8a8a;
    --card: #ffffff;
    --ink: #2b2b2b;
    --brand-blue: #1a4de6;
    --band-deep: #0a22f0;
    --band-light: #4f86ff;
    --shadow: rgba(0, 0, 0, 0.55);
  }
  * { margin: 0; padding: 0; box-sizing: border-box; }
  html, body {
    width: 981px; height: 1200px; overflow: hidden;
    background: var(--board);
    font-family: "Exo 2", "Arial", sans-serif;
  }
  .board { position: relative; width: 981px; height: 1200px; }
  .card {
    position: absolute;
    background: var(--card);
    box-shadow: 14px 16px 18px var(--shadow);
    overflow: visible;
  }
  .card--front { left: 73px; top: 79px; width: 832px; height: 486px; }
  .card--back  { left: 76px; top: 643px; width: 829px; height: 486px; }

  .brand-name {
    color: var(--brand-blue);
    font-weight: 800;
    text-transform: uppercase;
    line-height: 1;
    letter-spacing: 0.5px;
  }
  .card--front .brand-name {
    position: absolute; left: 22px; top: 52px;
    font-size: 34px;
  }
  .card--front .brand-name span { display: block; font-size: 20px; margin-top: 6px; letter-spacing: 2px; }

  .holder {
    position: absolute; right: 22px; top: 76px;
    font-size: 33px; font-weight: 800; color: var(--ink);
    text-transform: uppercase; letter-spacing: 1px;
  }
  .details {
    position: absolute; right: 22px; top: 182px;
    text-align: right; font-size: 21px; color: var(--ink);
    text-transform: uppercase; line-height: 33px; letter-spacing: 0.5px;
  }
  .band {
    position: absolute; left: 0; top: 343px; width: 835px; height: 143px;
  }
  .band-email {
    position: absolute; right: 22px; top: 401px;
    font-size: 20px; color: #ffffff; text-transform: uppercase; letter-spacing: 0.3px;
  }

  .card--back .brand-name {
    position: absolute; left: 0; right: 0; top: 190px;
    text-align: center; font-size: 66px;
  }
  .card--back .brand-name span { display: block; font-size: 34px; margin-top: 10px; letter-spacing: 5px; }
</style>
</head>
<body>
<main class="board">
  <section class="card card--front">
    <div class="brand-name">Crestline<span>Gas &amp; Plumbing</span></div>
    <h1 class="holder">Dale Whitcombe</h1>
    <div class="details">
      <p>Phone no : 0455163027</p>
      <p>ABN - 68204915336</p>
    </div>
    <svg class="band" viewBox="0 0 835 143" preserveAspectRatio="none" aria-hidden="true">
      <defs>
        <linearGradient id="bandShade" x1="0" y1="0" x2="0" y2="1">
          <stop offset="0" stop-color="#0a22f0"/>
          <stop offset="0.5" stop-color="#4f86ff"/>
          <stop offset="1" stop-color="#0a22f0"/>
        </linearGradient>
      </defs>
      <rect x="0" y="0" width="835" height="143" fill="url(#bandShade)"/>
      <path d="M0 0 H95 C150 30 160 110 110 143 H0 Z" fill="#ffffff"/>
    </svg>
    <p class="band-email">admin@crestlinegasandplumbing.example.com.au</p>
  </section>

  <section class="card card--back">
    <div class="brand-name">Crestline<span>Gas &amp; Plumbing</span></div>
  </section>
</main>
</body>
</html>
```